Business Card for Jewelry Business

We need a new namecard design for a jewelry company based in Bangkok, Thailand. We have a new website recently and want the new namecard to reflect our new modern image. I have uploaded our old namecard to show you the information that needs to be on the namecard. Pls check our website www.qelnotrax.com for the new color scheme to help design the new namecard.

```html
<!DOCTYPE html>
<html lang="en">
<head>
<meta charset="utf-8">
<title>Qelnotrax Manufacturers – Business Card</title>
<link rel="stylesheet" href="https://fonts.googleapis.com/css2?family=Sorts+Mill+Goudy&display=swap">
<style>
  :root {
    --teal: #4bbcc4;
    --teal-deep: #3aa9b2;
    --teal-ink: #3fb0b8;
    --paper: #ffffff;
    --paper-shade: #ececec;
    --ink: #2b2b2b;
    --ink-soft: #4a4a4a;
    --stage: #3a3a3c;
  }
  * { box-sizing: border-box; margin: 0; padding: 0; }
  html, body { width: 1200px; height: 900px; overflow: hidden; }
  body {
    background: var(--stage);
    font-family: "Sorts Mill Goudy", serif;
    position: relative;
  }
  .card {
    position: absolute;
    left: 250px;
    width: 700px;
    height: 400px;
    border-radius: 34px;
    overflow: hidden;
  }

  /* Front */
  .card-front {
    top: 40px;
    background: linear-gradient(135deg, var(--teal-deep), var(--teal));
    color: var(--paper);
  }
  .front-brand {
    position: absolute;
    top: 120px;
    left: 0; right: 0;
    display: flex;
    justify-content: center;
    align-items: center;
    gap: 14px;
    font-size: 40px;
    letter-spacing: 4px;
  }
  .brand-dot {
    width: 18px; height: 18px;
    border-radius: 50%;
    background: var(--paper);
  }
  .front-rule {
    position: absolute;
    left: 120px; right: 120px;
    height: 1.5px;
    background: var(--paper);
  }
  .front-rule.upper { top: 210px; }
  .front-rule.lower { top: 300px; }
  .social-row {
    position: absolute;
    top: 236px;
    left: 0; right: 0;
    display: flex;
    justify-content: center;
    gap: 40px;
    font-size: 22px;
  }
  .social-item { display: flex; align-items: center; gap: 10px; }
  .social-square {
    width: 22px; height: 22px;
    border-radius: 4px;
    background: var(--paper);
    opacity: 0.85;
  }

  /* Back */
  .card-back {
    top: 470px;
    background: linear-gradient(110deg, var(--paper-shade), var(--paper) 70%);
    color: var(--ink);
  }
  .back-brand {
    position: absolute;
    top: 40px;
    right: 50px;
    display: flex;
    align-items: center;
    gap: 12px;
    color: var(--ink);
  }
  .back-brand .brand-dot { background: var(--teal-ink); width: 16px; height: 16px; }
  .back-brand-name { font-size: 28px; letter-spacing: 2px; line-height: 1; }
  .back-brand-sub { font-size: 11px; letter-spacing: 2px; margin-top: 4px; text-align: right; }

  .holder { position: absolute; top: 120px; left: 50px; }
  .holder-name {
    font-size: 32px;
    color: var(--teal-ink);
    letter-spacing: 1px;
    text-transform: uppercase;
  }
  .holder-title { font-size: 19px; color: var(--ink-soft); margin-top: 2px; }

  .contact-list {
    position: absolute;
    top: 222px;
    left: 50px;
    list-style: none;
    font-size: 17px;
    color: var(--ink);
  }
  .contact-list li {
    display: flex;
    align-items: flex-start;
    gap: 12px;
    line-height: 22px;
  }
  .contact-list svg {
    width: 16px; height: 16px;
    margin-top: 3px;
    flex: none;
    fill: var(--teal-ink);
  }
  .contact-address { margin-top: 2px; }
</style>
</head>
<body>

<section class="card card-front">
  <div class="front-brand"><span class="brand-dot"></span>QELNOTRAX</div>
  <div class="front-rule upper"></div>
  <div class="social-row">
    <span class="social-item"><span class="social-square"></span>@QelnotraxCo</span>
    <span class="social-item"><span class="social-square"></span>Qelnotrax Manufacturers</span>
  </div>
  <div class="front-rule lower"></div>
</section>

<section class="card card-back">
  <div class="back-brand">
    <span class="brand-dot"></span>
    <div>
      <div class="back-brand-name">QELNOTRAX</div>
      <div class="back-brand-sub">MANUFACTURERS</div>
    </div>
  </div>

  <div class="holder">
    <h1 class="holder-name">Nalin Thavorn</h1>
    <p class="holder-title">Sales &amp; Product Development Manager</p>
  </div>

  <ul class="contact-list">
    <li>
      <svg viewBox="0 0 16 16"><path d="M3 1h3l1.5 4-2 1.3a9 9 0 0 0 4.2 4.2L11 8.5 15 10v3a2 2 0 0 1-2 2A12 12 0 0 1 1 3a2 2 0 0 1 2-2z"/></svg>
      <span>+662-410-5273</span>
    </li>
    <li>
      <svg viewBox="0 0 16 16"><path d="M4 1h8v4H4zM1 6h14v7h-3v2H4v-2H1zm4 5v3h6v-3z"/></svg>
      <span>+662-518-2964</span>
    </li>
    <li>
      <svg viewBox="0 0 16 16"><path d="M8 1a7 7 0 1 0 0 14A7 7 0 0 0 8 1zm0 1.5c.8 0 1.8 1.7 2.1 4.5H5.9C6.2 4.2 7.2 2.5 8 2.5zM2.6 7h2A11 11 0 0 1 5.3 3 5.6 5.6 0 0 0 2.6 7zm0 2a5.6 5.6 0 0 0 2.7 4 11 11 0 0 1-.7-4zm3.3 0h4.2c-.3 2.8-1.3 4.5-2.1 4.5S6.2 11.8 5.9 9zm5.5 0h2a5.6 5.6 0 0 1-2.7 4 11 11 0 0 0 .7-4zm2-2h-2a11 11 0 0 0-.7-4 5.6 5.6 0 0 1 2.7 4z"/></svg>
      <span>www.qelnotrax.com / hello@qelnotrax.com</span>
    </li>
    <li>
      <svg viewBox="0 0 16 16"><path d="M1 3h14v10H1zm1.5 1.5v.4L8 9l5.5-4.1v-.4zm0 2.3v4.7h11V6.8L8 10.9z"/></svg>
      <span>nalin@qelnotrax.com</span>
    </li>
    <li class="contact-address">
      <svg viewBox="0 0 16 16"><path d="M8 0a5.5 5.5 0 0 0-5.5 5.5C2.5 10 8 16 8 16s5.5-6 5.5-10.5A5.5 5.5 0 0 0 8 0zm0 7.5a2 2 0 1 1 0-4 2 2 0 0 1 0 4z"/></svg>
      <span>Qelnotrax Manufacturers Co., Ltd<br>128 Moo 7 Suwinthawong Road, Export Processing Zone 2,<br>Nong Chok Industrial Estate, Bangkok, 10530 Thailand</span>
    </li>
  </ul>
</section>

</body>
</html>
```